Meadowlark Educational Developmental Services (MEDS)

BI-Fold Brochure
1st page of brochure I want my name and logo of my company. I also want my picture Marguerite Holloway - CEO and Desmond Pickett - Executive Director with descriptions of ourselves.
2nd page of brochure names our Professional Development that MEDS offers. We have 9 different PD's and are willing to provide PD on the weekend as well.
3rd page of brochure talks about our mentoring program with a paragraph of "why" mentoring is important for At-Risk children ages 8-18. "Lantern Raising Program" for males and "Women of Courage & Harmony" (W.O.C.H.) for our females. Mentioning our 4 different programs - "Summer School Program", "After School Program", In School Youth/Mentor Program", and "In School Youth/Adult Mentor Program with P.D.".
4th page of brochure will be Testimonials and 2 pictures of our mentors with children. Phone numbers, website, email address.

Target Market(s)

We are looking for school districts/ companies/corporations/wealthy individuals that are interested in sponsoring our programs for At-Risk youth and for sponsoring At-Risk schools that are failing.

Font styles to use
Serif

Colors

Designer to choose colors to be used in the design.

Requirements
Must have
• When people are looking at the MEDS brochure I want them to have a "good feeling". What MEDS consultants do are to "uplift" the individuals and schools that we work with. All MEDS consultants are college educated professionals and all of MEDS mentors for At-Risk are individuals who were mentored themselves when young.
Nice to have
• Your input - ideas!

```html
<!DOCTYPE html>
<html lang="en">
<head>
<meta charset="utf-8">
<title>MEDS – Brochure Cover</title>
<link rel="stylesheet" href="https://fonts.googleapis.com/css2?family=Montserrat:wght@400;700&family=Lato:wght@300&display=swap">
<style>
  :root {
    --canvas: #e6e6e6;
    --paper: #ffffff;
    --sky-blue: #5577c9;
    --navy: #233e7a;
    --brand-navy: #1f3a7a;
    --slate: #8a8b8f;
    --mist: #e2e0de;
    --ink: #1f1f1f;
    --tagline: #6e6e6e;
    --white: #ffffff;
  }
  * { margin: 0; padding: 0; box-sizing: border-box; }
  html, body {
    width: 884px; height: 1200px; overflow: hidden;
    background: var(--canvas);
  }
  .cover {
    position: absolute; left: 84px; top: 82px;
    width: 713px; height: 1011px;
    background: var(--paper);
    overflow: hidden;
  }
  .cover-shapes { position: absolute; inset: 0; width: 713px; height: 1011px; }
  .brand {
    position: absolute; left: 262px; top: 84px;
    display: flex; align-items: center; gap: 14px;
    color: var(--brand-navy);
    font-family: "Montserrat", sans-serif; font-weight: 700;
    font-size: 22px; line-height: 28px;
  }
  .brand-mark { width: 28px; height: 28px; flex: none; background: var(--brand-navy); }
  .person { position: absolute; font-family: "Montserrat", sans-serif; }
  .person-name { font-weight: 700; font-size: 14.5px; }
  .person-role { font-weight: 400; font-size: 12.5px; margin-top: 1px; }
  .person--ceo { left: 272px; top: 346px; color: var(--white); }
  .person--director { left: 383px; top: 716px; color: var(--ink); }
  .web-address {
    position: absolute; left: 299px; top: 604px;
    font-family: "Montserrat", sans-serif; font-weight: 700;
    font-size: 19px; color: var(--white);
  }
  .tagline {
    position: absolute; left: 16px; top: 858px; width: 540px;
    text-align: center;
    font-family: "Lato", sans-serif; font-weight: 300;
    font-size: 32px; line-height: 36px; color: var(--tagline);
  }
</style>
</head>
<body>
  <main class="cover">
    <svg class="cover-shapes" viewBox="0 0 713 1011">
      <defs>
        <linearGradient id="ceo-photo-tone" x1="0" y1="0" x2="1" y2="1">
          <stop offset="0" stop-color="#6c8ad3"/>
          <stop offset="0.55" stop-color="#b9a98c"/>
          <stop offset="1" stop-color="#2a2a2e"/>
        </linearGradient>
        <linearGradient id="director-photo-tone" x1="0" y1="0" x2="1" y2="1">
          <stop offset="0" stop-color="#ecebea"/>
          <stop offset="0.6" stop-color="#8a6a58"/>
          <stop offset="1" stop-color="#1e2230"/>
        </linearGradient>
      </defs>
      <g transform="translate(-84,-82)">
        <polygon class="panel-ceo" points="84,147 587,438 84,728" fill="var(--sky-blue)"/>
        <polygon role="img" aria-label="Portrait photo of Marguerite Holloway, Chief Executive Officer"
                 points="84,200 420,394 420,534 84,728" fill="url(#ceo-photo-tone)"/>
        <polygon class="panel-slate" points="390,570 592,452 592,688" fill="var(--slate)"/>
        <polygon class="panel-sky" points="607,455 797,565 607,683" fill="var(--sky-blue)"/>
        <polygon class="panel-navy" points="84,742 375,578 583,697 84,985" fill="var(--navy)"/>
        <polygon class="panel-director" points="797,595 412,815 797,1038" fill="var(--mist)"/>
        <polygon role="img" aria-label="Portrait photo of Desmond Pickett, Executive Director"
                 points="548,737 797,595 797,1038 548,894" fill="url(#director-photo-tone)"/>
      </g>
    </svg>

    <header class="brand">
      <span class="brand-mark"></span>
      <span class="brand-name">Meadowlark Educational<br>Developmental Services</span>
    </header>

    <div class="person person--ceo">
      <p class="person-name">Marguerite Holloway</p>
      <p class="person-role">Chief Executive Officer</p>
    </div>

    <p class="web-address">medsed.com</p>

    <div class="person person--director">
      <p class="person-name">Desmond Pickett</p>
      <p class="person-role">Executive Director</p>
    </div>

    <p class="tagline">The best way to get<br>connected with consultants<br>in your industry!</p>
  </main>
</body>
</html>
```